Velora Aesthetica

Medical doctor providing aesthetic medicine

* Double sided card
* Logo to be on card
Other details:
* Dr. Mirela Kostvan, BSc, MBChB, CCFP
* #214-215, 27903 83 Ave, Surrey, BC, V2T 4K7
* 604-718-2943
* info@veloraclinic.ca
* www.veloraclinic.ca

Industry/Entity Type

Medical / Health & Beauty

Contact Information for Business Card

see 'Project Description'

Colors
0054AA
0677BA
7BADD7
CADEEF
E8F1F8
FFF300
FFF600
FEFA6F
FFFEC7
FFFEE8

Requirements
Must have
• Modern, high-end design

```html
<!DOCTYPE html>
<html lang="en">
<head>
<meta charset="utf-8">
<title>Velora Aesthetica – Business Card</title>
<link rel="stylesheet" href="https://fonts.googleapis.com/css2?family=Montserrat:wght@400;500;600;700&display=swap">
<style>
  :root {
    --page-bg: #d3d4d6;
    --navy-dark: #1f3a58;
    --navy-light: #27496d;
    --navy-band: #213d5b;
    --gold: #d4a82a;
    --gold-light: #e6c04a;
    --white: #ffffff;
    --ink: #141414;
  }
  * { box-sizing: border-box; margin: 0; padding: 0; }
  html, body { width: 900px; height: 1200px; overflow: hidden; }
  body {
    background: var(--page-bg);
    font-family: "Montserrat", sans-serif;
    position: relative;
  }
  .card {
    position: absolute;
    left: 135px;
    width: 631px;
    border-radius: 14px;
    overflow: hidden;
  }
  .card-front {
    top: 215px;
    height: 357px;
    background: linear-gradient(120deg, var(--navy-dark), var(--navy-light));
  }
  .card-back {
    top: 628px;
    height: 358px;
    background: var(--white);
  }
  .brand {
    position: absolute;
    left: 0; right: 0;
    display: flex;
    flex-direction: column;
    align-items: center;
  }
  .brand-ring {
    border: 3px solid var(--gold);
    border-radius: 50%;
  }
  .brand-name {
    font-weight: 500;
    text-transform: uppercase;
    white-space: nowrap;
  }
  .card-front .brand { top: 92px; }
  .card-front .brand-ring { width: 118px; height: 118px; margin-bottom: 40px; }
  .card-front .brand-name {
    color: var(--white);
    font-size: 27px;
    letter-spacing: 0.28em;
    padding-left: 0.28em;
  }
  .card-back .brand { left: auto; right: 20px; width: 300px; top: 86px; }
  .card-back .brand-ring { width: 96px; height: 96px; margin-bottom: 36px; }
  .card-back .brand-name {
    color: var(--ink);
    font-size: 17px;
    letter-spacing: 0.22em;
    padding-left: 0.22em;
  }
  .details {
    position: absolute;
    left: 37px;
    top: 86px;
    color: var(--ink);
  }
  .person-name {
    font-size: 24px;
    font-weight: 600;
    letter-spacing: 0.01em;
    text-transform: uppercase;
  }
  .credentials {
    color: var(--gold);
    font-size: 15px;
    font-weight: 600;
    margin-top: 4px;
    letter-spacing: 0.03em;
  }
  .address {
    font-size: 14.5px;
    line-height: 22px;
    margin-top: 14px;
    font-style: normal;
  }
  .contact-list { list-style: none; margin-top: 10px; }
  .contact-item {
    display: flex;
    align-items: center;
    gap: 7px;
    font-size: 15px;
    height: 25px;
    letter-spacing: 0.02em;
  }
  .contact-item.phone { letter-spacing: 0.14em; }
  .contact-icon { width: 11px; height: 11px; fill: var(--gold); flex: none; }
  .wave { position: absolute; left: 0; bottom: 0; width: 631px; height: 358px; }
</style>
</head>
<body>

  <section class="card card-front" aria-label="Card front">
    <div class="brand">
      <div class="brand-ring"></div>
      <div class="brand-name">Velora Aesthetica</div>
    </div>
  </section>

  <section class="card card-back" aria-label="Card back">
    <div class="details">
      <h1 class="person-name">Dr. Mirela Kostvan</h1>
      <p class="credentials">BSc, MBChB, CCFP</p>
      <address class="address">#214-215, 27903 83 Ave,<br>Surrey, BC, V2T 4K7</address>
      <ul class="contact-list">
        <li class="contact-item phone">
          <svg class="contact-icon" viewBox="0 0 24 24"><path d="M6.6 10.8a15.1 15.1 0 0 0 6.6 6.6l2.2-2.2c.3-.3.7-.4 1-.2 1.1.4 2.3.6 3.6.6.6 0 1 .4 1 1V20c0 .6-.4 1-1 1A17 17 0 0 1 3 4c0-.6.4-1 1-1h3.5c.6 0 1 .4 1 1 0 1.3.2 2.5.6 3.6.1.3 0 .7-.2 1z"/></svg>
          604-718-2943
        </li>
        <li class="contact-item">
          <svg class="contact-icon" viewBox="0 0 24 24"><path d="M2 5h20v14H2z M2 5l10 8 10-8" fill="none" stroke="#d4a82a" stroke-width="3"/></svg>
          info@veloraclinic.ca
        </li>
        <li class="contact-item">
          <svg class="contact-icon" viewBox="0 0 24 24"><g fill="none" stroke="#d4a82a" stroke-width="2"><circle cx="12" cy="12" r="10"/><ellipse cx="12" cy="12" rx="4" ry="10"/><path d="M2 12h20M4 7h16M4 17h16"/></g></svg>
          www.veloraclinic.ca
        </li>
      </ul>
    </div>

    <div class="brand">
      <div class="brand-ring"></div>
      <div class="brand-name">Velora Aesthetica</div>
    </div>

    <svg class="wave" viewBox="0 0 631 358" aria-hidden="true">
      <path fill="var(--navy-band)" d="M0,298 C100,325 210,345 300,344 C400,343 500,300 560,292 C600,286 620,300 631,312 L631,358 L0,358 Z"/>
      <path fill="var(--gold)" d="M0,288 C80,314 170,337 262,345 C170,335 80,315 0,296 Z"/>
      <path fill="var(--gold-light)" d="M520,289 C580,270 615,278 631,296 L631,306 C612,288 575,281 520,289 Z"/>
    </svg>
  </section>

</body>
</html>
```